Small Web Design for Boat Industry

We are looking for a small 4 page web site. The designs will need to be clean and stylish. Please see samples of sites that we like.

http://www.verimont.co.uk/
http://gildwaxer.com/

We need a quick turnaround.

• Please see attached documents with all wording and images

```html
<!DOCTYPE html>
<html lang="en">
<head>
<meta charset="utf-8">
<title>Moorlink – Docking Poles for Boats</title>
<link href="https://fonts.googleapis.com/css2?family=Open+Sans:ital,wght@0,400;0,600;0,700;1,400&display=swap" rel="stylesheet">
<style>
:root{
  --black:#000;
  --ink:#333;
  --muted:#666;
  --blue:#1b5e9c;
  --sky:#3f9bd6;
  --red:#c90000;
  --brand:#d8283a;
  --panel:#2d2d2d;
  --footer:#2f2f2f;
  --line:#d6d6d6;
  --pale:#f4f4f4;
}
*{box-sizing:border-box;margin:0;padding:0}
html,body{width:814px;height:1200px;overflow:hidden;background:#fff}
body{position:relative;font-family:Arial,Helvetica,sans-serif;color:var(--ink)}
.abs{position:absolute}

.topbar{left:0;top:0;width:814px;height:47px;background:var(--black)}
.brand{left:67px;top:11px;font-family:'Open Sans',Arial,sans-serif;font-weight:700;font-size:19px;line-height:24px;color:var(--brand)}
.nav{top:18px;font-family:'Open Sans',Arial,sans-serif;font-size:8.5px;color:#fff;font-weight:600}

.hero{left:0;top:47px;width:814px;height:359px;background:linear-gradient(180deg,#b26a3e 0%,#d98f57 30%,#8a5a40 62%,#3b2c2a 100%)}
.hero-title{left:421px;top:200px;width:330px;font-family:'Open Sans',Arial,sans-serif;font-weight:700;font-size:14.5px;line-height:22px;color:#fff;text-transform:uppercase;text-shadow:0 1px 3px rgba(0,0,0,.6)}
.hero-arrows{left:687px;top:335px;width:56px;height:27px;display:flex;gap:1px}
.hero-arrows span{flex:1;background:rgba(60,40,30,.55);display:flex;align-items:center;justify-content:center}

.welcome{left:67px;top:372px;width:680px;height:122px;background:var(--panel);box-shadow:0 14px 14px -8px rgba(0,0,0,.35)}
.welcome-photo{left:67px;top:372px;width:198px;height:122px;background:linear-gradient(135deg,#f3f3f3,#dadada)}
.welcome-title{left:301px;top:398px;font-family:'Open Sans',Arial,sans-serif;font-weight:700;font-size:11px;color:#fff}
.welcome-text{left:301px;top:419px;width:425px;font-family:'Open Sans',Arial,sans-serif;font-size:7px;line-height:17px;color:#bbb}

.section-title{font-family:'Open Sans',Arial,sans-serif;font-weight:700;font-size:10px;color:var(--blue)}
.faq-item{left:67px;width:256px;height:26px;border:1px solid var(--line);font-size:7.5px;color:#222;padding:0 11px;display:flex;align-items:center;justify-content:space-between}
.faq-item i{font-style:normal;color:#999;font-size:7px;letter-spacing:1px}
.faq-answer{left:74px;top:610px;width:240px;font-size:6.7px;line-height:14.5px;color:#555}
.faq-answer b{font-weight:400;color:var(--blue)}

.fender-photo{left:367px;top:578px;width:171px;height:104px;background:linear-gradient(160deg,#d8e2ea 0%,#6f8c93 45%,#2f4a46 100%)}
.fender-sub{left:561px;top:575px;width:160px;font-family:'Open Sans',Arial,sans-serif;font-weight:400;font-size:9.5px;line-height:16px;color:var(--sky)}
.fender-text{font-size:6.5px;line-height:15.2px;color:#555}

.cta{left:67px;top:788px;width:680px;height:53px;background:var(--pale);border:1px solid #e2e2e2}
.cta-text{left:85px;top:799px;width:530px;font-family:'Open Sans',Arial,sans-serif;font-style:italic;font-size:8px;line-height:16px;color:#555}
.cta-btn{left:630px;top:798px;width:105px;height:32px;background:var(--red);color:#fff;font-family:'Open Sans',Arial,sans-serif;font-weight:700;font-size:10.5px;display:flex;align-items:center;justify-content:center;border-radius:2px}

.videos-intro{left:72px;top:870px;font-family:'Open Sans',Arial,sans-serif;font-size:8px;color:#444}
.videos-intro strong{font-size:10px;color:var(--blue)}
.video-thumb{top:905px;height:135px;display:flex;align-items:center;justify-content:center}
.video-title{top:1053px;font-family:'Open Sans',Arial,sans-serif;font-weight:700;font-size:9.5px;color:#333}
.video-desc{top:1074px;font-size:7px;color:#666}

.footer{left:0;top:1125px;width:814px;height:75px;background:var(--footer)}
.footer-links{left:69px;top:1148px;font-size:7px;color:#fff}
.footer-links span{margin:0 14px;color:#ccc}
.copyright{left:69px;top:1169px;font-size:7px;color:#fff}
.social-label{left:540px;top:1158px;font-size:7px;color:#fff}
.social{top:1152px;width:19px;height:19px;border-radius:50%;background:#5a5a5a}
</style>
</head>
<body>

<header>
  <div class="abs topbar"></div>
  <div class="abs brand">Moorlink</div>
  <nav>
    <div class="abs nav" style="left:406px">HOME</div>
    <div class="abs nav" style="left:475px">FAQS</div>
    <div class="abs nav" style="left:540px">VIDEOS</div>
    <div class="abs nav" style="left:613px">CONTACT US</div>
    <div class="abs nav" style="left:707px">BUY NOW</div>
  </nav>
</header>

<section>
  <div class="abs hero" role="img" aria-label="Marina at sunset with city towers behind moored boats"></div>
  <h1 class="abs hero-title">Moorlink is a new, fast and easy system for temporally docking boats</h1>
  <div class="abs hero-arrows">
    <span><svg width="10" height="14" viewBox="0 0 10 14"><path d="M8 1 2 7l6 6" fill="none" stroke="#fff" stroke-width="1.5"/></svg></span>
    <span><svg width="10" height="14" viewBox="0 0 10 14"><path d="M2 1l6 6-6 6" fill="none" stroke="#fff" stroke-width="1.5"/></svg></span>
  </div>
</section>

<section>
  <div class="abs welcome"></div>
  <div class="abs welcome-photo" role="img" aria-label="Black docking pole with metal end ring"></div>
  <h2 class="abs welcome-title">WELCOME TO MOORLINK</h2>
  <p class="abs welcome-text">Moorlink is a new, fast and easy system for temporally docking boats reducing the need for fenders. Designed to keep boats off of docks, Moorlinks will impress you with how quickly you can connect your boat. Measuring just 63cm long and 8cm in diameter Moorlinks are easy to store and take up just a fraction of the space that fenders require.</p>
</section>

<section>
  <h2 class="abs section-title" style="left:67px;top:544px">FAQ’S</h2>
  <div class="abs faq-item" style="top:574px">Do these work on all docks?<i>[ - ]</i></div>
  <p class="abs faq-answer">Most but not all. Moorlinks can be adapted to work in most situations. You can use rope to extend or change the method of connection. The important factor is the angle of use. They must have the opportunity to extend and contract, so if the angle is too steep or the distance... <b>[ Raed more ]</b></p>
  <div class="abs faq-item" style="top:680px">How do I connect these to my boat and the dock?<i>[ + ]</i></div>
  <div class="abs faq-item" style="top:708px">Can I use your product to permanently connect my boat ...<i>[ + ]</i></div>
  <div class="abs faq-item" style="top:736px">I have a 28 ft. boat. Will these work for me?<i>[ + ]</i></div>
</section>

<section>
  <h2 class="abs section-title" style="left:366px;top:544px">REVOLUTIONARY BOAT FENDERS!</h2>
  <div class="abs fender-photo" role="img" aria-label="Docking pole holding a white boat hull away from a dock over green water"></div>
  <h3 class="abs fender-sub">Lorem Ipsum is simply dummy text of printing...</h3>
  <p class="abs fender-text" style="left:561px;top:610px;width:180px">Moorlink is a new, fast and easy system for temporally docking boats reducing the need for fenders. Designed to keep boats off of docks, Moorlinks will impress you with how quickly you can connect your boat. Measureing just 63cm long and 8cm in diameter Moorlinks are easy</p>
  <p class="abs fender-text" style="left:371px;top:695px;width:380px">to store and take up just a fraction of the space that fenders require. These units are durable and can be adapted to work with many types of boats. They can be ordered individually but if this is your first time ordering we do recommend you order two for the most secure docking. Also, if you order two you will receive a free Storage Bag. Please contact us if you have any questions.</p>
</section>

<section>
  <div class="abs cta"></div>
  <p class="abs cta-text">Content here, content here', making it look like readable English. Many desktop publishing packages and web page editors now use Lorem Ipsum as their default model text...</p>
  <a class="abs cta-btn">BUY NOW</a>
</section>

<section>
  <p class="abs videos-intro"><strong>OUR VIDEOS</strong> Here are some connection ideas for using our product. Moorlinks are adaptable to most docking situations.</p>

  <div class="abs video-thumb" style="left:67px;width:226px;background:linear-gradient(180deg,#9cb6c9 0%,#3f6b86 45%,#cfd3d4 100%)" role="img" aria-label="Video still of a speedboat tied alongside a floating dock">
    <svg width="22" height="22" viewBox="0 0 22 22"><rect width="22" height="22" fill="rgba(0,0,0,.35)"/><path d="M8 6l8 5-8 5z" fill="#5fb0e0"/></svg>
  </div>
  <div class="abs video-thumb" style="left:294px;width:225px;background:linear-gradient(135deg,#fafafa 0%,#d9d9d9 60%,#efefef 100%)" role="img" aria-label="Video still of two black docking poles with metal rings">
    <svg width="22" height="22" viewBox="0 0 22 22"><rect width="22" height="22" fill="rgba(0,0,0,.35)"/><path d="M8 6l8 5-8 5z" fill="#5fb0e0"/></svg>
  </div>
  <div class="abs video-thumb" style="left:521px;width:226px;background:linear-gradient(135deg,#b9ab96 0%,#e6e1d8 55%,#f5f5f5 100%)" role="img" aria-label="Video still of a person kneeling on a dock attaching a pole to a boat">
    <svg width="22" height="22" viewBox="0 0 22 22"><rect width="22" height="22" fill="rgba(0,0,0,.35)"/><path d="M8 6l8 5-8 5z" fill="#5fb0e0"/></svg>
  </div>

  <h3 class="abs video-title" style="left:68px">LOREM IPSUM IS A DUMMY TEXT</h3>
  <p class="abs video-desc" style="left:68px">Here are some connection ideas for using our product.</p>
  <h3 class="abs video-title" style="left:295px">LOREM IPSUM IS A DUMMY TEXT</h3>
  <p class="abs video-desc" style="left:295px">Here are some connection ideas for using our product.</p>
  <h3 class="abs video-title" style="left:522px">LOREM IPSUM IS A DUMMY TEXT</h3>
  <p class="abs video-desc" style="left:522px">Here are some connection ideas for using our product.</p>
</section>

<footer>
  <div class="abs footer"></div>
  <p class="abs footer-links">Home<span>/</span>FAQs<span>/</span>Videos<span>/</span>Contact Us<span>/</span>Buy Now</p>
  <p class="abs copyright">© 2015 - Moorlink - All rights reserved.</p>
  <p class="abs social-label">Connect with our social network :</p>
  <span class="abs social" style="left:650px"></span>
  <span class="abs social" style="left:674px"></span>
  <span class="abs social" style="left:700px"></span>
  <span class="abs social" style="left:726px"></span>
</footer>

</body>
</html>
```